Global Nano Technology Surface Protection company needs a new logo and cards

We are a Global company that will apply nanotechnology coatings on surfaces to prevent growth and spread of bacteria, viruses, mold etc. We deal with large corporates, airlines, hospitals and schools so we are after a new modern, simple and clean look that will have great visual impact.
We a company that is focused on prevention and protection.

Company name, Quorvane Systems Worldwide

Subtext, Antimicrobial Surface Protection

Logo, QVSW or QSW

Target Market(s)

Hospitals, Transport agencies, Airlines, Corporate entities

Industry/Entity Type

Protection

Contact Information for Business Card

Logo, QVSW or QSW
www.qvsw-example.us
Derek Holloway
+64290536218
tidyshieldnz@mailbox-example.com

Logo Text

QVSW

Requirements
Must have
• Simple clean look
Should not have
• Nothing too messy

```html
<!DOCTYPE html>
<html lang="en">
<head>
<meta charset="utf-8">
<title>Quorvane Systems Worldwide — Business Cards</title>
<link rel="stylesheet" href="https://fonts.googleapis.com/css2?family=Josefin+Sans:wght@400;700&family=Raleway:wght@400;500;800&display=swap">
<style>
  :root {
    --backdrop: #e4e5e6;
    --lime: #bcd631;
    --leaf: #8fb52a;
    --ink: #2b2b2b;
    --paper: #ffffff;
    --soft-ink: #3a3a3a;
  }
  * { box-sizing: border-box; margin: 0; padding: 0; }
  html, body {
    width: 1200px;
    height: 799px;
    overflow: hidden;
    background: var(--backdrop);
  }
  .canvas {
    position: relative;
    width: 1200px;
    height: 799px;
    display: flex;
    align-items: center;
    justify-content: center;
    gap: 40px;
  }
  .card {
    position: relative;
    width: 525px;
    height: 300px;
    box-shadow: 0 6px 18px rgba(0,0,0,0.18);
    display: flex;
    flex-direction: column;
    align-items: center;
  }

  /* Front: contact side */
  .card--contact {
    background: var(--lime);
    color: var(--paper);
    padding-top: 38px;
  }
  .contact__name {
    font-family: "Josefin Sans", sans-serif;
    font-weight: 700;
    font-size: 23px;
    letter-spacing: 0.04em;
    text-transform: uppercase;
  }
  .contact__phone {
    font-family: "Josefin Sans", sans-serif;
    font-size: 12px;
    letter-spacing: 0.08em;
    margin-top: 2px;
  }
  .brand-mark {
    display: flex;
    align-items: center;
    gap: 8px;
    font-family: "Raleway", sans-serif;
    font-weight: 500;
    letter-spacing: 0.3em;
  }
  .brand-mark__dot {
    border-radius: 50%;
    flex: none;
  }
  .card--contact .brand-mark {
    margin-top: 52px;
    font-size: 26px;
    color: var(--paper);
  }
  .card--contact .brand-mark__dot {
    width: 14px;
    height: 14px;
    background: var(--paper);
  }
  .contact__details {
    margin-top: auto;
    margin-bottom: 34px;
    text-align: center;
    font-family: "Josefin Sans", sans-serif;
    font-size: 13px;
    line-height: 1.45;
    letter-spacing: 0.03em;
  }

  /* Back: company side */
  .card--company {
    background: var(--paper);
    color: var(--ink);
    justify-content: center;
  }
  .card--company .brand-mark {
    font-size: 28px;
    color: var(--leaf);
  }
  .card--company .brand-mark__dot {
    width: 16px;
    height: 16px;
    background: var(--leaf);
  }
  .company__name {
    margin-top: 30px;
    font-family: "Raleway", sans-serif;
    font-weight: 800;
    font-size: 24px;
    line-height: 1.1;
    text-align: center;
    text-transform: uppercase;
    color: var(--ink);
  }
  .company__tagline {
    margin-top: 14px;
    font-family: "Raleway", sans-serif;
    font-weight: 400;
    font-size: 12px;
    letter-spacing: 0.04em;
    text-transform: uppercase;
    color: var(--soft-ink);
  }
</style>
</head>
<body>
<main class="canvas">
  <article class="card card--contact">
    <h1 class="contact__name">Derek Holloway</h1>
    <p class="contact__phone">+64290536218</p>
    <div class="brand-mark"><span class="brand-mark__dot"></span>QVSW</div>
    <p class="contact__details">
      tidyshieldnz@mailbox-example.com<br>
      www.qvsw-example.com
    </p>
  </article>

  <article class="card card--company">
    <div class="brand-mark"><span class="brand-mark__dot"></span>QVSW</div>
    <h2 class="company__name">Quorvane Systems<br>Worldwide</h2>
    <p class="company__tagline">Antimicrobial Surface Protection</p>
  </article>
</main>
</body>
</html>
```